Web Design Project for Professional/Social Media Networking website

www.SteeringTapestry.com.au

I am launching a professional/social media networking website called SteeringTapestry which raises awareness of Diversity topics that impact professional, education and social communities. The Diversity initiative targets gender, age, disability, sexual orientation, race and ethnicity.

I expect the majority of customers will be professional women aged 18-65 across all industries. This brand is designed to empower, support and promote those people under represented across the specified diversity groups. It will appeal to those looking to improve both their professional & personal lives. This will be a platform or organisations to promote themselves on the website, therefore, this must be a high quality professional looking site.

I am looking for a website that is professional, positive and has impact. This project is for the design and coding of the website. I have an idea what I want to see but also open to creative design on presentation of items, various pages and flow.

The coding will consist of making the design function (not just pretty pictures). We would be looking to have the winner work with us on a going forward basis for website design changes, tweaks or modifications (paid of course). Please be honest with regards to programming/coding experience and skills as the functionality/ease of this website is essential to its success.

Key Objectives
•Build brand awareness and assist in providing synergy with all key marketing strategies.
•Create a fresh and compelling website design reflecting what the business stands for it will also be user-friendly, build the company’s corporate image and appeal to defined target markets.
•Generate search engine compatibility by optimizing the site for all the major search engines.
•Integrate a custom Content Management System (CMS) to ensure all updates can be made with ease, improving operational efficiency and reducing time to market with critical information.
•Social media implantation, to create social awareness and increase repeat visitors to the site

Customers:
*Australian market initially then branching out Internationally

Must Have:
Company logo-Attached

Inspiration
This website will have a bit of a WorkLoop style functionality. http://www.tradewrens.com.au is another good example of the type of functionality I’m looking for. I understand that the functionality will need to be adapted and increased overtime; however, I am looking for the following minimal features:

Option 1l Page craft CMS Design l (Eg: tradewrens.com.au)

Complete Custom Design
User Friendly Navigation Strategy
Information capture forms (Contact Us)
Rotating banner of images on the home page
CMS - Content Management System to make edits and changes
Membership Area
Blog Integration
Calender & Events Integration
Social Media Plugins
Gallery By Category
Custom URL Structures
Multi-level Navigation
Unlimited Pages Via CMS
uMobe & USlate Compatibility

Option 2 l Custom CMS Design

Complete Custom Design
Membership Area
Directory Listing
Calender Integration for Upcoming Events
Search Functionality ( Tagging System : Individual Profile & business )
Basic SEO Integration
Quorra Metrics
Blog Integration
Forum Integration
Search Engine Submission
Social Media Basic Integration, Pinbook, Chirpex etc.
Custom URL Structures
Multi-level Navigation
Unlimited Pages Via CMS

Option 2 would be my preference, however, guidance on the length of time, cost etc would be welcome. I am happy to increase the budget if required as I appreciate there will be more work involved.

I am looking for the home page to be something different with more of a wow factor and something different to the standard page link menu across the top of the screen.

For the home page I am looking for something a little more striking with a visual impact.

Overall
* Not looking for a cookie cutter template
* Home page simplistic and smooth that shows our "brand"
* Modern browser compatible, CSS, Tablet friendly
* FAST Loading, mouseover buttons, custom icons where necessary

Pages Requested in Design (style, fonts, icons, images, etc flow from page to page).
Home Page
Search Results/directory
Members area/profiles of members
About us
Contact Us
News/features
Updates

Industry/Entity Type

Education

Requirements
Must have
• Logo must be at the Top of each webpage

```html
<!DOCTYPE html>
<html lang="en">
<head>
<meta charset="utf-8">
<title>SteeringTapestry — Home</title>
<link rel="stylesheet" href="https://fonts.googleapis.com/css2?family=Questrial&family=Arimo:wght@400;700&display=swap">
<style>
:root{
  --navy:#1f2866;
  --title-blue:#2d3588;
  --link-blue:#2450a8;
  --text:#2e2e2e;
  --muted:#8a8a8a;
  --line:#dedede;
  --panel-bg:#ffffff;
  --nav-top:#ffffff;
  --nav-bottom:#eef1f4;
  --nav-accent:#cddcea;
  --orange:#f29b1d;
  --cal-bg:#eeeeee;
  --cal-active:#6b6b6b;
  --heading:"Questrial",sans-serif;
  --body:"Arimo",sans-serif;
}
*{box-sizing:border-box;margin:0;padding:0}
html,body{width:966px;height:1200px;overflow:hidden}
body{background:linear-gradient(#f1f1f1 0,#ffffff 60px);font-family:var(--body);color:var(--text);position:relative}
a{color:inherit;text-decoration:none}
h2,h3{font-weight:400}

.panel{position:absolute;background:var(--panel-bg);border:1px solid var(--line)}
.panel-title{font-family:var(--heading);font-weight:400;font-size:10.5px;letter-spacing:.2px;color:#111;height:30px;line-height:30px;border-bottom:1px solid var(--line);margin:0 8px;padding-left:5px}

/* header */
.site-header{position:absolute;left:143px;top:6px;width:679px;height:106px;background:#fff;border:1px solid #e6e6e6}
.brand{position:absolute;left:8px;top:8px;width:140px;text-align:center}
.brand-mark{display:block;width:39px;height:39px;border-radius:50%;background:#1f5fa9;margin:0 auto 5px}
.brand-name{font-family:var(--heading);font-size:13.5px;color:var(--navy)}
.account-links{position:absolute;right:8px;top:13px;font-family:var(--heading);font-size:8.5px;color:var(--muted);letter-spacing:.2px}
.account-links span{margin:0 5px}
.search{position:absolute;left:512px;top:35px;width:158px;height:21px;border:1px solid #d4d4d4;background:#fafafa}
.search-label{position:absolute;left:6px;top:5px;font-family:var(--heading);font-size:8.5px;color:#999}
.search-btn{position:absolute;right:0;top:0;width:20px;height:19px;border-left:1px solid #ddd}
.main-nav{position:absolute;left:-1px;top:73px;width:679px;height:33px;display:flex;background:linear-gradient(var(--nav-top),var(--nav-bottom));border-bottom:3px solid var(--nav-accent)}
.main-nav a{font-family:var(--heading);font-size:11px;color:#777;line-height:31px;text-align:center;border-right:1px solid #e0e0e0}
.main-nav a:last-child{border-right:0}
.main-nav a.active{background:var(--navy);color:#fff}

/* hero */
.hero{position:absolute;left:143px;top:120px;width:468px;height:204px;background:radial-gradient(ellipse at 70% 40%,#8fa2b8 0,#4b6382 30%,#1c3456 60%,#0d1e38 100%);overflow:hidden}
.hero-caption{position:absolute;left:0;bottom:0;width:100%;height:44px;background:rgba(5,14,30,.55);padding:5px 8px}
.hero-title{font-family:var(--heading);font-size:10.5px;color:var(--orange)}
.hero-text{font-size:7.5px;color:#fff;line-height:11.5px;width:300px;margin-top:1px}
.hero-arrows{position:absolute;right:13px;bottom:10px}

/* membership */
.membership{left:619px;top:120px;width:203px;height:204px}
.field-label{position:absolute;left:11px;font-family:var(--heading);font-size:8.5px;color:#777}
.field{position:absolute;left:11px;width:179px;height:21px;border:1px solid #d6d6d6;background:linear-gradient(#f7f7f7,#fff)}
.login-btn{position:absolute;left:11px;top:139px;width:56px;height:22px;background:var(--navy);color:#fff;font-family:var(--heading);font-size:8.5px;text-align:center;line-height:22px;border:1px solid #0f1440}
.forgot{position:absolute;left:11px;top:169px;font-size:8px;color:var(--link-blue)}
.remember{position:absolute;left:11px;top:184px;font-size:8px;color:#999;display:flex;align-items:center;gap:4px}
.remember i{display:inline-block;width:8px;height:8px;border:1px solid #ccc}

/* blog */
.blog{left:143px;top:331px;width:469px;height:457px}
.post{margin:0 8px;padding:8px 5px 12px;border-bottom:1px solid var(--line);height:132px}
.post-title{font-family:var(--heading);font-weight:400;font-size:11px;line-height:15px;color:var(--title-blue);height:30px}
.post-body{display:flex;gap:6px;margin-top:7px}
.post-thumb{width:75px;height:75px;flex:none;border:1px solid #ccc}
.post-copy{display:flex;flex-direction:column;height:75px}
.post-copy p{font-size:7.6px;line-height:15px;margin-top:-4px}
.post-meta{margin-top:auto;display:flex;gap:30px;font-size:8px;color:var(--muted);align-items:center}
.post-meta span{display:flex;align-items:center;gap:4px}
.read-more{font-size:8px;color:var(--navy);position:absolute;left:16px}

/* forum */
.forum{left:143px;top:794px;width:469px;height:300px}
.topic{margin:0 8px;padding:8px 5px 0;border-bottom:1px solid var(--line);height:62px}
.topic h3{font-family:var(--heading);font-weight:400;font-size:11px;color:var(--title-blue);line-height:14px}
.topic p{font-size:7.6px;line-height:15px;margin-top:1px}

/* events */
.events{left:619px;top:331px;width:203px;height:211px}
.calendar{position:absolute;left:7px;top:35px;width:188px;height:168px;background:var(--cal-bg);border:1px solid #e0e0e0;border-radius:5px;padding:8px 10px 0}
.cal-head{display:flex;justify-content:space-between;font-size:8.5px;color:#555;height:18px}
.cal-head b{font-weight:700;color:#555}
.cal-grid{display:grid;grid-template-columns:repeat(7,23.5px);row-gap:3px;justify-content:center}
.cal-grid .dow{font-size:8.5px;color:#999;text-align:center;height:13px;line-height:18px}
.cal-grid .day{width:21px;height:15px;background:#fff;border:1px solid #e3e3e3;font-size:8px;line-height:13px;text-align:center;color:#555;position:relative}
.cal-grid .day.other{color:#ccc}
.cal-grid .day.today{background:var(--cal-active);color:#fff;border-color:#555}
.cal-grid .day.has-event::after{content:"";position:absolute;left:3px;bottom:1px;border-left:3px solid transparent;border-bottom:3px solid var(--orange)}

/* fan box */
.fanbox{left:619px;top:550px;width:203px;height:224px}
.fan-mark{position:absolute;left:4px;top:6px;width:31px;height:31px;border-radius:50%;background:#1f5fa9}
.fan-name{position:absolute;left:40px;top:8px;font-size:8.5px;color:var(--title-blue);font-weight:700}
.fan-name small{font-weight:400;font-size:7px;color:var(--link-blue)}
.fan-like{position:absolute;left:40px;top:22px;width:31px;height:13px;border:1px solid #c8cde0;background:#eef0f6;font-size:7px;color:#3b5090;text-align:center;line-height:11px}
.fan-count{position:absolute;left:6px;top:45px;width:190px;border-top:1px solid var(--line);padding-top:5px;font-size:7px;color:#333}
.fan-count b{font-size:8px}
.fans{position:absolute;left:6px;top:62px;display:grid;grid-template-columns:repeat(5,34px);column-gap:3.6px;row-gap:16px}
.fan{width:34px;height:34px;position:relative}
.fan span{position:absolute;top:36px;left:-4px;width:42px;text-align:center;font-size:6px;color:#777}
.fan-plugin{position:absolute;left:6px;top:204px;width:190px;border-top:1px solid var(--line);padding-top:3px;font-size:6px;color:#777;display:flex;align-items:center;gap:4px}
.fan-plugin i{width:8px;height:8px;background:#3b5090;display:inline-block}

/* chirps */
.chirps{left:619px;top:781px;width:203px;height:313px}
.chirp{margin:0 3px;padding:8px 8px 0 8px;border-bottom:1px solid var(--line)}
.chirp p{font-size:7.8px;line-height:12.2px}
.chirp p em{font-style:normal;color:#888}
.chirp-actions{font-size:7px;color:var(--link-blue);margin-top:6px;display:flex;gap:6px;padding-bottom:6px}

/* share bar */
.rule{position:absolute;left:143px;top:1110px;width:679px;height:1px;background:var(--line)}
.share-bar{position:absolute;left:143px;top:1124px;width:679px;height:22px;border:1px solid #ccc;display:flex;align-items:center;padding:0 7px;font-size:7px;color:#555}
.chip{border:1px solid #c9c9c9;background:#f4f4f4;height:12px;line-height:10px;padding:0 3px;font-size:7px;margin-right:3px}
.chip.like{color:#3b5090}
.chip.plus{color:#c0392b}
.chip.save{color:#b0202a;margin-left:auto}
.follow{font-family:var(--heading);font-size:7px;color:var(--navy);margin-left:10px}
.follow b{font-size:11px;font-weight:400}
.follow.chirp-follow{color:#2a9fd6}
.follow-btn{margin-left:10px;border:1px solid #c9c9c9;background:#f6e4e4;color:#b0202a;font-size:6.5px;padding:1px 4px}

/* footer */
.site-footer{position:absolute;left:143px;top:1155px;width:679px;height:36px}
.footer-mark{position:absolute;left:0;top:0;width:35px;height:35px;border-radius:50%;background:#777}
.footer-links{position:absolute;left:44px;top:6px;font-size:8px;color:#666}
.footer-copy{position:absolute;left:44px;top:18px;font-size:8px;color:#666}
</style>
</head>
<body>

<header class="site-header">
  <a class="brand" href="#"><i class="brand-mark"></i><span class="brand-name">SteeringTapestry</span></a>
  <div class="account-links">BECOME A MEMBER<span>|</span>LOG IN</div>
  <div class="search">
    <span class="search-label">SEARCH</span>
    <span class="search-btn"><svg width="20" height="19" viewBox="0 0 20 19"><circle cx="9" cy="8.5" r="4" fill="none" stroke="#999" stroke-width="1.4"/><line x1="12" y1="11.5" x2="15.5" y2="15" stroke="#999" stroke-width="1.6"/></svg></span>
  </div>
  <nav class="main-nav">
    <a href="#" style="width:57.6px">HOME</a>
    <a href="#" class="active" style="width:66.4px">ARTICLES</a>
    <a href="#" style="width:62.4px">EVENTS</a>
    <a href="#" style="width:88px">COMMUNITY</a>
    <a href="#" style="width:98.4px">COMPETITIONS</a>
    <a href="#" style="width:69.6px">GALLERY</a>
    <a href="#" style="width:75.2px">PARTNERS</a>
    <a href="#" style="width:72px">ABOUT US</a>
    <a href="#" style="width:89.6px">CONTACT US</a>
  </nav>
</header>

<section class="hero" role="img" aria-label="Rotating banner photo: close portrait of a woman with pale hair in cool blue light">
  <div class="hero-caption">
    <div class="hero-title">Quisque vehicula libero et urna ultricies vel lacinia mauris imperdiet.</div>
    <div class="hero-text">Duis tristique sodales purus ac lacinia. Duis velit justo, iaculis vitae congue ac, elementum ac tellus.</div>
  </div>
  <svg class="hero-arrows" width="48" height="24" viewBox="0 0 48 24"><polyline points="14,2 4,12 14,22" fill="none" stroke="#fff" stroke-width="4.5"/><polyline points="34,2 44,12 34,22" fill="none" stroke="#fff" stroke-width="4.5"/></svg>
</section>

<aside class="panel membership">
  <h2 class="panel-title">MEMBERSHIP AREA</h2>
  <span class="field-label" style="top:43px">USERNAME</span>
  <span class="field" style="top:57px"></span>
  <span class="field-label" style="top:90px">PASSWORD</span>
  <span class="field" style="top:104px"></span>
  <a class="login-btn" href="#">LOGIN</a>
  <a class="forgot" href="#">Forgot Password ?</a>
  <span class="remember"><i></i>Remember me</span>
</aside>

<section class="panel blog">
  <h2 class="panel-title">BLOG UPADTES</h2>
  <article class="post">
    <h3 class="post-title">Praesent varius, massa sit amet luctus congue, felis urna adipiscing justo, non feugiat urna eros et leo.</h3>
    <div class="post-body">
      <div class="post-thumb" role="img" aria-label="Fashion photo of a woman in black and white with pink lettering" style="background:linear-gradient(90deg,#f1c9d6,#d9d4d4 45%,#5a5458)"></div>
      <div class="post-copy">
        <p>Maecenas vitae arcu ipsum. Pellentesque sed convallis lacus. Vestibulum ac dui non tellus feugiat mattis vitae nec purus. Phasellus eros turpis, scelerisque sed imperdiet sit amet, laoreet eu velit. Pellentesque volutpat leo elementum sapien placerat mattis.Donec sodales neque convallis tellus imperdiet ac ullamcorper nulla dictum.</p>
        <div class="post-meta"><span><svg width="8" height="8"><rect x=".5" y="1.5" width="7" height="6" fill="none" stroke="#999"/><line x1="0" y1="3.5" x2="8" y2="3.5" stroke="#999"/></svg>November 7, 2012</span><span><svg width="10" height="8"><ellipse cx="5" cy="3.5" rx="4.5" ry="3.2" fill="#999"/><polygon points="2,5 1,8 5,6" fill="#999"/></svg>0 Comments</span></div>
      </div>
    </div>
  </article>
  <article class="post">
    <h3 class="post-title">Felis urna adipiscing justo, non feugiat urna eros et leo. Praesent varius, massa sit amet luctus congue,</h3>
    <div class="post-body">
      <div class="post-thumb" role="img" aria-label="Photo of two sportsmen in navy training gear" style="background:linear-gradient(160deg,#7f95a8,#2f3a55 55%,#1a2033)"></div>
      <div class="post-copy">
        <p>Vestibulum ac dui non tellus feugiat mattis vitae nec purus. Phasellus eros turpis, scelerisque sed imperdiet sit amet, laoreet eu velit. Pellentesque volutpat leo elementum sapien placerat mattis.Donec sodales neque convallis tellus imperdiet ac ullamcorper nulla dictum. Maecenas vitae arcu ipsum. Pellentesque sed convallis lacus.</p>
        <div class="post-meta"><span><svg width="8" height="8"><rect x=".5" y="1.5" width="7" height="6" fill="none" stroke="#999"/><line x1="0" y1="3.5" x2="8" y2="3.5" stroke="#999"/></svg>November 7, 2012</span><span><svg width="10" height="8"><ellipse cx="5" cy="3.5" rx="4.5" ry="3.2" fill="#999"/><polygon points="2,5 1,8 5,6" fill="#999"/></svg>0 Comments</span></div>
      </div>
    </div>
  </article>
  <article class="post">
    <h3 class="post-title">Aipiscing justo, non feugiat urna eros et leo. Praesent varius, massa sit amet luctus congue, felis urna</h3>
    <div class="post-body">
      <div class="post-thumb" role="img" aria-label="Photo of ballet dancers performing on stage" style="background:linear-gradient(180deg,#5c79b5,#8fa0c8 50%,#c9a98f)"></div>
      <div class="post-copy">
        <p>Scelerisque sed imperdiet sit amet, laoreet eu velit. Pellentesque volutpat leo elementum sapien placerat mattis.Donec sodales neque convallis tellus imperdiet ac ullamcorper nulla dictum. Maecenas vitae arcu ipsum. Pellentesque sed convallis lacus. Vestibulum ac dui non tellus feugiat mattis vitae nec purus. Phasellus eros turpis,</p>
        <div class="post-meta"><span><svg width="8" height="8"><rect x=".5" y="1.5" width="7" height="6" fill="none" stroke="#999"/><line x1="0" y1="3.5" x2="8" y2="3.5" stroke="#999"/></svg>November 7, 2012</span><span><svg width="10" height="8"><ellipse cx="5" cy="3.5" rx="4.5" ry="3.2" fill="#999"/><polygon points="2,5 1,8 5,6" fill="#999"/></svg>0 Comments</span></div>
      </div>
    </div>
  </article>
  <a class="read-more" href="#" style="top:438px">Read more Blogs...</a>
</section>

<section class="panel forum">
  <h2 class="panel-title">FORUM</h2>
  <article class="topic"><h3>Massa sit amet luctus congue, felis urna adipiscing justo, non feugiat urna eros et leo.</h3><p>Pellentesque sed convallis lacus. Vestibulum ac dui non tellus feugiat mattis vitae nec purus. Phasellus eros turpis, scelerisque sed imperdiet sit amet, laoreet eu velit.</p></article>
  <article class="topic"><h3>Luctus congue, felis urna adipiscing justo, non feugiat urna eros et leo.</h3><p>Convallis lacus. Vestibulum ac dui non tellus feugiat mattis vitae nec purus. Phasellus eros turpis, scelerisque sed imperdiet sit amet, laoreet eu velit.</p></article>
  <article class="topic"><h3>Congue, felis urna adipiscing justo, non feugiat urna eros et leo.</h3><p>Vestibulum ac dui non tellus feugiat mattis vitae nec purus. Phasellus eros turpis, scelerisque sed imperdiet sit amet, laoreet eu velit.</p></article>
  <article class="topic" style="height:58px"><h3>Felis urna adipiscing justo, non feugiat urna eros et leo.</h3><p>Scelerisque sed imperdiet sit amet, laoreet eu velit. Pellentesque sed convallis lacus. Vestibulum ac dui non tellus feugiat mattis vitae nec purus. Phasellus eros turpis,</p></article>
  <a class="read-more" href="#" style="top:281px">Read more...</a>
</section>

<aside class="panel events">
  <h2 class="panel-title">UPCOMING EVENTS</h2>
  <div class="calendar">
    <div class="cal-head"><span>«</span><b>November 2012</b><span>»</span></div>
    <div class="cal-grid">
      <span class="dow">Su</span><span class="dow">Mo</span><span class="dow">Tu</span><span class="dow">We</span><span class="dow">Th</span><span class="dow">Fr</span><span class="dow">Sa</span>
      <span class="day other">25</span><span class="day other">26</span><span class="day other">27</span><span class="day other">28</span><span class="day other">29</span><span class="day other">30</span><span class="day">1</span>
      <span class="day">2</span><span class="day">3</span><span class="day">4</span><span class="day">5</span><span class="day">6</span><span class="day">7</span><span class="day">8</span>
      <span class="day">9</span><span class="day">10</span><span class="day">11</span><span class="day">12</span><span class="day">13</span><span class="day">14</span><span class="day">15</span>
      <span class="day">16</span><span class="day">17</span><span class="day has-event">18</span><span class="day">19</span><span class="day">20</span><span class="day today">21</span><span class="day">22</span>
      <span class="day">23</span><span class="day">24</span><span class="day">25</span><span class="day">26</span><span class="day">27</span><span class="day">28</span><span class="day">29</span>
      <span class="day">30</span><span class="day other">1</span><span class="day other">2</span><span class="day other">3</span><span class="day other">4</span><span class="day other">5</span><span class="day other">6</span>
    </div>
  </div>
</aside>

<aside class="panel fanbox">
  <i class="fan-mark"></i>
  <div class="fan-name">SteeringTapestry <small>on Pinbook</small></div>
  <div class="fan-like">Like</div>
  <div class="fan-count">16,838 people like <b>SteeringTapestry</b></div>
  <div class="fans">
    <div class="fan" role="img" aria-label="Member photo" style="background:#7a4a3a"><span>Corinne</span></div>
    <div class="fan" role="img" aria-label="Member photo" style="background:#c9a48c"><span>Casimir</span></div>
    <div class="fan" role="img" aria-label="Member photo" style="background:#4a3328"><span>Maribel</span></div>
    <div class="fan" role="img" aria-label="Member photo" style="background:#3a4a78"><span>Alenoti</span></div>
    <div class="fan" role="img" aria-label="Member photo" style="background:#8c8880"><span>Clarisse</span></div>
    <div class="fan" role="img" aria-label="Member photo" style="background:#8aa0b0"><span>Stellan</span></div>
    <div class="fan" role="img" aria-label="Member photo" style="background:#3d8fc4"><span>Jolene</span></div>
    <div class="fan" role="img" aria-label="Member photo" style="background:#9c8070"><span>Dot</span></div>
    <div class="fan" role="img" aria-label="Member photo" style="background:#5a7ab0"><span>Storage</span></div>
    <div class="fan" role="img" aria-label="Member photo" style="background:#c06a5a"><span>Lu</span></div>
    <div class="fan" role="img" aria-label="Member photo" style="background:#8a5a48"><span>Kerry</span></div>
    <div class="fan" role="img" aria-label="Member photo" style="background:#a89880"><span>Mireille</span></div>
    <div class="fan" role="img" aria-label="Member photo" style="background:#5a6a80"><span>Lenny</span></div>
    <div class="fan" role="img" aria-label="Member photo" style="background:#b08a60"><span>Kit</span></div>
    <div class="fan" role="img" aria-label="Member photo" style="background:#6a4a40"><span>Katalin</span></div>
  </div>
  <div class="fan-plugin"><i></i>Pinbook social plugin</div>
</aside>

<aside class="panel chirps">
  <h2 class="panel-title">CHIRPEX UPDATES</h2>
  <div class="chirp"><p>Curabitur fringilla tellus molestie lacus faucibus at imperdiet dolor luctus. Nunc ornare, est id elementum pellentesque, <em>@ felis nunc euismod libero, a fringilla justo libero at tortor.</em></p><div class="chirp-actions"><span>Reply</span><span>Rechirped</span><span>Favorite</span></div></div>
  <div class="chirp"><p>Vivamus faucibus viverra pulvinar. Donec mollis facilisis vulputate. Mauris et feugiat nisl. Duis purus nisi, <em>@ venenatis ac pellentesque in, commodo id nisl.</em></p><div class="chirp-actions" style="padding-bottom:7px"><span>Reply</span><span>Rechirped</span><span>Favorite</span></div></div>
  <div class="chirp" style="height:98px"><p>Viverra pulvinar. Donec mollis facilisis vulputate. Mauris et feugiat nisl. Duis purus nisi, viverra pulvinar. Donec mollis facilisis vulputate.<em>@ ac pellentesque in, commodo id nisl.</em></p><div class="chirp-actions"><span>Reply</span><span>Rechirped</span><span>Favorite</span></div></div>
  <a class="read-more" href="#" style="top:295px;left:10px">More Chirps...</a>
</aside>

<div class="rule"></div>
<div class="share-bar">
  <span class="chip like">Like</span><span class="chip">1.1k</span>
  <span class="chip plus" style="margin-left:8px">+1</span><span>+8</span>
  <span class="chip save">Save</span><span class="chip">3</span>
  <span class="follow">BE A FAN ON <b>Pinbook</b></span>
  <span class="follow chirp-follow">FOLLOW US ON <b>Chirpex</b></span>
  <span class="follow-btn">Follow me on Pinora</span>
</div>

<footer class="site-footer">
  <i class="footer-mark"></i>
  <div class="footer-links">Home | Articles | Events | Community | Competitions | Gallery | Partners | About Us | Contact Us</div>
  <div class="footer-copy">Copyright © 2012 Steering Tapestry, All Rights Reserved</div>
</footer>

</body>
</html>
```